Modern, crisp, funky web 2.0 site required for childrens holiday programmes

We want a new "Wow" website. Please help this become a reality.

Funtrek is a provider of childrens holiday programmes aimed primary at children 5yrs to 12 yrs. You can view our current site at www.funtrek.co.nz

This website is a primarily a booking portal. Parents typically come to the website to register and book for courses after having seen them in a booklet. However we are changing the marketing approach and are now trying to attract parents directly to the website. Therefore we want the website to be very graphically appealing, very easy to browse and navigate and must be easy to register and book.

The front end is what is being re-designed. The new front end MUST be compatible with the existing back-end system and processes and the back-end should not need to be changed at all. People lodging a tender must familiarise themselves with the existing site and ensure that the new front end will be fully compatible.

The site must be PHP

This tender will not include a re-design of the logo. Please use the current logo which is attached with this document.

Everything else is up for re-design. The site needs a new, clean, crisp modern design. (See Likes and Dislikes).

Some yellow must be used somewhere within the colour scheme to be in keeping with the brand colours. However no yellow background please.

We currently operate in 2 main regions: Auckland and Palmerston North. However we will be adding new regions soon. The website should make it easy for users to find courses in their region easily.

We also offer term time activities – the site needs another area for that. Perhaps emulated as another “region”.

Beyond that courses are offered across a range of activities. Ideally the website would organise courses logically so that users can find what they are looking for easily.

However, if possible it would be good for the user to be able to browse by area. For example within Auckland there would be North Shore, Central, West, East and South. Within each area a range of course are available – e.g. Skateboarding, Surfing etc. However we don’t want this to be the primary design goal. This is more a “could have” than a “must have”

Once the user has found the course they want the site needs to have a course identification button / tab / box e.g. Tennis. Once the user has clicked through all the details pertaining to the tennis courses on offer should be presented. People are used to searching the existing website in this manner.

When clients click through from the course they have chosen to book the GREEN box that’s say “More Info” needs to be changed to say Book Now

Needs to the ability to have photos displayed on each page next to course descriptions or a panel of photos showing the children doing the activity displayed on that page.

Needs the ability to select the “Pick up locations” To show up in the booking form and class attendance sheet e.g. 7.45am/4.45pm: Harbourview Burgerbarn Carpark. In front of Burgerbarn by the shopping trundler bay.
8.10am/4.10pm: Tolley Cove Reserve, Ridgefield Road, Marlowton in the car park in form of the tennis courts

Needs to have Course options above the line (at the top of the page)

Needs to have a description of Funtrek below the line (at the bottom of the page)

You can provide stock images but they must be New Zealand activities (i.e. not American Football) and pre-approved by us. Alternatively we can supply some images.

What adjectives should best describe your website design?
Clean, modern, professional, vibrant, both kid and adult appealing, fun, interesting

What content must be included in the website design?

• Home page
• Contact us
• Testimonials
• Terms and conditions
• New customer sign or log in
• My account or existing client log in
• Chatterbook button,
• Sign up to the newsletter (postparrot)
• Refer a friend option – where they input a friend’s contact details, we then send them a one-off email “from” the friend with a HTML email describing our website. Content of the email must be able to be modified easily later (by a programmer).
• “Become a course provider” enquiry tab. This could be a simple form which emails details through.
• Have “View latest booklet” tab which downloads a PDF of the booklet after submitting the users email address onto our PostParrot mailing list (must offer postparrot integration).
• Must support Zenmetric analytics data collection
Updates

Reason: I have not really seen anything that greatly excites me. I am concerned we re not getting the level of design work in as committed to on the starting up stage we only have 18 designs (Many from the same designer and repeats) I was expecting closer to 50. Please can you assist and advise as to how to improve the results thanks Dana

Target Market(s)

Parents, both working and stay at home, children aged 5-15 years of age with middle – high income.

Industry/Entity Type

Marketing

Requirements
Must have
• The site must be easy to use and navigate.

Users need to be able to navigate with the minimal number of clicks as the site is used by busy mums with no patience!

Users should be able to find exactly what they want with absolute ease.

Needs to be appealing to children aged 5 – 12 years old as well as parents of children within that age range.

Needs to have lots of images of children doing the activities offered. Should NOT have cartoon images!

Must be able to written in PHP – this is to enable it to be compatible with the existing back-end.

Likes:

Big Icons
Clean, crisp design
Vivid, striking in appearance
Uncluttered
Easy to navigate
Social Media integration
Modern
Not much ‘below the line’
Thematically consistent
Easily modifiable pictures and content
Like real images
Search bar would be good if effective ONLY

What colours do you want to see in your website design?
The Yellow in the logo BUT NOT as the background, purple as in the balls etc on logo, white for clean and simple easy to read, black for writing and other areas for details ie boarders etc.
Should not have
• Dislikes:

Cartoon images – must be real images.
Moving, floating in and out and spinning pictures text or photos
Clutter
Underlining
Intentionally misspelt words and typos
Content ‘below the line’ on the Home page
Backgrounds ending before the edge of the screen

What colours do you NOT want to see in your website design?
Browns, pink, pastel colours, mustard, pale yellow, and not a confusion of colours – must be themed and consistent.

```html
<!DOCTYPE html>
<html lang="en">
<head>
<meta charset="utf-8">
<title>Funtrek – Account Details</title>
<link href="https://fonts.googleapis.com/css2?family=Arimo:wght@400;700&family=Ubuntu:wght@400;500&family=Roboto+Condensed:wght@700&display=swap" rel="stylesheet">
<style>
:root{
  --page:#f0eee9;
  --panel:#ffffff;
  --purple:#5f3392;
  --purple-dark:#4e2680;
  --ink:#1e1e1e;
  --muted:#555;
  --line:#b9b9b9;
  --teal:#1aa7b0;
  --yellow:#d8d21c;
  --blue:#6ea6e8;
}
*{box-sizing:border-box;margin:0;padding:0}
html,body{width:1200px;height:1008px;overflow:hidden}
body{background:var(--page);font-family:Arimo,Arial,sans-serif;color:var(--ink);position:relative}
.abs{position:absolute}

/* header */
.brand{left:100px;top:38px;display:flex;align-items:center;gap:10px}
.brand-dot{width:34px;height:34px;border-radius:50%;background:var(--yellow)}
.brand-name{font-family:Ubuntu,sans-serif;font-weight:500;font-size:58px;color:#2b2b2b;letter-spacing:-1px}
.utility{right:107px;top:16px;font-family:Ubuntu,sans-serif;font-size:15px}
.utility span{margin:0 3px}
.social{top:101px;left:738px;display:flex;align-items:center;font-family:Ubuntu,sans-serif;font-size:13px}
.social .bubble{margin:0 18px 0 8px}
.social .sq{width:24px;height:24px;margin-left:13px;border-radius:2px}
.sq1{background:#3b5ea8}.sq2{background:#bdbdbd}.sq3{background:#c9302c}

/* nav */
.mainnav{left:0;top:145px;width:1200px;height:51px;background:linear-gradient(var(--purple) 70%,var(--purple-dark))}
.mainnav a{position:absolute;top:16px;color:#fff;text-decoration:none;font-family:Arimo,sans-serif;font-size:18px;letter-spacing:.2px}

/* sidebar */
.search-box{left:105px;top:210px;width:231px;height:336px;background:var(--panel);box-shadow:0 0 4px rgba(0,0,0,.15)}
.search-box h2{position:absolute;left:13px;top:12px;font-family:"Roboto Condensed",sans-serif;font-size:17px;letter-spacing:.2px}
.lbl{font-size:14px;position:absolute}
.field{position:absolute;height:22px;border:1px solid var(--line);background:#fff}
.field .arr{position:absolute;right:0;top:0;width:22px;height:100%;background:#e6e6e6;border-left:1px solid var(--line)}
.field .arr:after{content:"";position:absolute;left:6px;top:7px;border:5px solid transparent;border-top:7px solid #888}
.field .cal{position:absolute;right:5px;top:5px;width:10px;height:10px;border:1px solid #777}
.btn-filter{position:absolute;left:14px;top:293px;width:202px;height:24px;background:var(--purple);color:#fff;font-weight:700;font-size:13px;text-align:center;line-height:24px}
.news{left:108px;top:557px;width:228px;height:87px;background:var(--purple);color:#fff}
.news h2{position:absolute;left:13px;top:9px;font-family:"Roboto Condensed",sans-serif;font-size:17px}
.news .in{position:absolute;left:10px;top:34px;width:201px;height:22px;background:#fff;border:1px solid #999}
.news .hint{position:absolute;left:13px;top:64px;font-size:14px}
.news .sub{position:absolute;right:18px;top:63px;background:#fff;color:#000;font-size:11px;border-radius:9px;padding:2px 7px;border:1px solid #888}
.phones{left:108px;top:659px;width:228px;height:137px;background:rgba(255,255,255,.6)}
.phones .city{position:absolute;left:25px;font-size:18px;color:#333}
.phones .num{position:absolute;left:22px;display:flex;align-items:center;gap:8px;font-size:24px;color:#333}

/* main panel */
.main{left:348px;top:210px;width:742px;height:696px;background:var(--panel);box-shadow:0 0 4px rgba(0,0,0,.15)}
.subnav{position:absolute;left:27px;top:14px;font-size:13.5px;font-weight:700;white-space:nowrap}
.subnav .on{color:var(--purple)}
.subnav span{margin-right:4px}
.welcome{position:absolute;left:27px;top:52px;font-size:17px;font-weight:700;color:var(--purple)}
.f-lbl{position:absolute;left:30px;font-size:12px;font-weight:700}
.inp{position:absolute;height:22px;border:1px solid var(--line);background:#fff;font-size:11px;padding:4px 3px}
.sel{position:absolute;height:17px;border:1px solid #8fa8c8;border-radius:4px;background:linear-gradient(#fff,#e7e7e7);font-size:11px;padding:1px 7px}
.sel:after{content:"";position:absolute;right:0;top:0;width:16px;height:100%;background:var(--blue);border-radius:0 3px 3px 0}
.req{position:absolute;color:var(--purple);font-size:16px;font-weight:700}
.note{position:absolute;left:30px;top:500px;font-size:10px;line-height:15px;width:140px}
.check{position:absolute;left:244px;display:flex;align-items:center;gap:6px;font-size:13px}
.check i{width:12px;height:12px;border:1px solid #888;border-radius:2px;display:inline-block;position:relative}
.check a{color:var(--teal);text-decoration:none}
.btn-update{position:absolute;left:34px;top:647px;width:152px;height:29px;background:var(--purple);color:#fff;font-weight:700;font-size:14px;text-align:center;line-height:29px}
.legend{position:absolute;left:237px;top:642px;color:var(--purple);font-weight:700;font-size:13.5px;line-height:17px}

/* footer */
.footlinks{left:107px;top:939px;font-size:14px}
.footrule{left:107px;top:961px;width:983px;height:1px;background:#555}
.footnote{left:107px;top:965px;font-size:14px}
</style>
</head>
<body>

<header>
  <div class="abs brand"><span class="brand-dot"></span><span class="brand-name">Funtrek</span></div>
  <nav class="abs utility"><span>Log out</span>I<span>Register</span>I<span>My Account</span>I<span>Shopping Cart</span></nav>
  <div class="abs social">
    Tell a Friend About Us
    <svg class="bubble" width="30" height="26" viewBox="0 0 30 26"><ellipse cx="15" cy="12" rx="13" ry="10" fill="#c05aa0"/><path d="M8 19 L5 25 L14 21Z" fill="#c05aa0"/></svg>
    Follow Us
    <span class="sq sq1" aria-label="Chatterbook"></span><span class="sq sq2" aria-label="Clipstream"></span><span class="sq sq3" aria-label="Circlenet"></span>
  </div>
</header>

<nav class="abs mainnav">
  <a style="left:113px">HOME</a><a style="left:199px">COURSES</a><a style="left:312px">TESTIMONIALS</a><a style="left:469px">TERMS AND CONDITIONS</a><a style="left:712px">BECOME A COURSE PROVIDER</a><a style="left:1002px">CONTACT</a>
</nav>

<aside>
  <div class="abs search-box">
    <h2>SEARCH &amp; BOOK A COURSE</h2>
    <span class="lbl" style="left:15px;top:43px">Location:</span>
    <div class="field" style="left:15px;top:62px;width:199px"><span class="arr"></span></div>
    <span class="lbl" style="left:15px;top:103px">Duration:</span>
    <div class="field" style="left:89px;top:99px;width:48px"><span class="arr"></span></div>
    <span class="lbl" style="left:15px;top:135px">Start date:</span>
    <div class="field" style="left:89px;top:132px;width:126px"><span class="cal"></span></div>
    <span class="lbl" style="left:15px;top:167px">End date:</span>
    <div class="field" style="left:89px;top:165px;width:126px"><span class="cal"></span></div>
    <span class="lbl" style="left:15px;top:198px">Select a course:</span>
    <div class="field" style="left:13px;top:218px;width:202px"><span class="arr"></span></div>
    <span class="lbl" style="left:15px;top:258px">Ages:</span>
    <div class="field" style="left:89px;top:254px;width:48px"><span class="arr"></span></div>
    <div class="btn-filter">Filter Courses</div>
  </div>

  <div class="abs news">
    <h2>NEWSLETTER SIGN UP</h2>
    <div class="in"></div>
    <span class="hint">Enter your email</span>
    <span class="sub">Submit</span>
  </div>

  <div class="abs phones">
    <span class="city" style="top:7px">Auckland</span>
    <div class="num" style="top:29px"><svg width="30" height="30" viewBox="0 0 30 30"><circle cx="15" cy="15" r="13" fill="none" stroke="#333" stroke-width="2"/><path d="M10 8 L13 8 L14 12 L12 13 Q13 17 17 18 L18 16 L22 17 L22 20 Q16 22 11 16 Q8 11 10 8Z" fill="#333"/></svg>555 0182</div>
    <span class="city" style="top:75px">Palmerston North</span>
    <div class="num" style="top:96px"><svg width="30" height="30" viewBox="0 0 30 30"><circle cx="15" cy="15" r="13" fill="none" stroke="#333" stroke-width="2"/><path d="M10 8 L13 8 L14 12 L12 13 Q13 17 17 18 L18 16 L22 17 L22 20 Q16 22 11 16 Q8 11 10 8Z" fill="#333"/></svg>555 0247</div>
  </div>
</aside>

<main class="abs main">
  <nav class="subnav"><span class="on">ACCOUNT DETAILS</span> <span>I PREVIOUS ACTIVITY</span> <span>I CHILD INFO</span> <span>I ADD CHILD I</span> <span>SHOPPING CART I</span> <span>LOG OUT</span></nav>
  <h1 class="welcome">Welcome John Doe</h1>

  <span class="f-lbl" style="top:99px">Title:</span>
  <div class="sel" style="left:236px;top:95px;width:58px">Mrs</div>

  <span class="f-lbl" style="top:132px">Name:</span>
  <div class="inp" style="left:236px;top:127px;width:155px">John</div><span class="req" style="left:394px;top:128px">*</span>

  <span class="f-lbl" style="top:165px">Surname:</span>
  <div class="inp" style="left:236px;top:160px;width:155px">Doe</div><span class="req" style="left:394px;top:161px">*</span>

  <span class="f-lbl" style="top:197px">Email:</span>
  <div class="inp" style="left:236px;top:193px;width:155px"></div><span class="req" style="left:394px;top:193px">*</span>

  <span class="f-lbl" style="top:230px">Address:</span>
  <div class="inp" style="left:236px;top:226px;width:175px;height:45px"></div>

  <span class="f-lbl" style="top:288px">City:</span>
  <div class="sel" style="left:236px;top:282px;width:154px">select</div>

  <span class="f-lbl" style="top:320px">Suburb:</span>
  <div class="sel" style="left:236px;top:315px;width:34px"></div>

  <span class="f-lbl" style="top:352px">PostCode:</span>
  <div class="sel" style="left:236px;top:347px;width:34px"></div>

  <span class="f-lbl" style="top:384px">Home Phone:</span>
  <div class="sel" style="left:236px;top:381px;width:65px">09</div>
  <div class="inp" style="left:305px;top:379px;width:156px">123123</div><span class="req" style="left:466px;top:379px">**</span>

  <span class="f-lbl" style="top:417px">Work Phone:</span>
  <div class="sel" style="left:236px;top:414px;width:65px">09</div>
  <div class="inp" style="left:305px;top:412px;width:156px">123456</div>

  <span class="f-lbl" style="top:450px">Mobile:</span>
  <div class="sel" style="left:236px;top:447px;width:65px">select</div>
  <div class="inp" style="left:305px;top:445px;width:156px"></div>

  <span class="f-lbl" style="top:482px">Change Password:</span>
  <p class="note">Please type your new password followed by the same password in the confirmation box.</p>
  <div class="inp" style="left:236px;top:477px;width:206px"></div>
  <div class="inp" style="left:236px;top:522px;width:206px"></div>
  <span style="position:absolute;left:446px;top:526px;font-size:12px;letter-spacing:.5px">[confirmation]</span>

  <label class="check" style="top:573px"><i><svg width="12" height="12" viewBox="0 0 12 12" style="position:absolute;left:0;top:-1px"><path d="M2 6 L5 9 L11 1" fill="none" stroke="#2b5fa8" stroke-width="2"/></svg></i>I agree to the <a>Terms and Conditions</a><span style="color:var(--purple);font-weight:700;font-size:16px">*</span></label>
  <label class="check" style="top:606px"><i></i>I want to receive the newsletter</label>

  <div class="btn-update">UPDATE DETAILS</div>
  <p class="legend">* Requested fields<br>** You must enter at least two phone numbers</p>
</main>

<footer>
  <p class="abs footlinks">Impressum I Terms and Conditions I Contact Us</p>
  <div class="abs footrule"></div>
  <p class="abs footnote">We accept Paycard and Globecard. For more assistance please contact us at: enquiries@funtrek.co.nz or call Auckland: 555 0182, Palmerston North: 555 0247</p>
</footer>

</body>
</html>
```